Business Card for Bright Meadow Lawn & Landscape

Double Sided Card Design - I think one side of the card should be cleaner, with logo, contact info, and "Complete Residential & Commercial Landscape Services", and on the other side it should list the services we offer:

- Lawn Care & Mowing
- Hedge & Shrub Trimming
- Leaf Removal & Clean Up
- Aeration & Sod
- Mulch & Rock Installations
- Landscape Installations & Renovations
- Commercial Snow Removal

Please make it clean and very professional... don't want it too be too busy, but want to tell them what we do.

Target Market(s)

Residential and Commercial

Industry/Entity Type

Landscape

Contact Information for Business Card

Fully Insured
Tom Berrigan
410-555-0198
Tberrigan07@mailbox-example.com

Requirements
Must have
• Double Sided, Cleaner on one side, more information and text on the other side.

```html
<!DOCTYPE html>
<html lang="en">
<head>
<meta charset="utf-8">
<title>Bright Meadow Lawn &amp; Landscape – Business Card</title>
<link rel="stylesheet" href="https://fonts.googleapis.com/css2?family=Cinzel:wght@600;700&family=Crimson+Text:wght@400;600&display=swap">
<style>
  :root {
    --bg: #2b2b2b;
    --card-black: #0b0b0b;
    --card-white: #ffffff;
    --green: #86bd3f;
    --text-light: #f2f2f2;
    --text-dark: #1a1a1a;
  }
  * { margin: 0; padding: 0; box-sizing: border-box; }
  html, body {
    width: 1200px; height: 880px; overflow: hidden;
    background: var(--bg);
  }
  .card {
    position: absolute; left: 250px;
    width: 700px; height: 400px;
    border-radius: 18px; overflow: hidden;
    box-shadow: 0 10px 30px rgba(0,0,0,.45);
  }
  .card svg.shapes { position: absolute; inset: 0; }
  .card-front { top: 30px; background: var(--card-black); }
  .card-back { top: 450px; background: var(--card-white); }

  .brand-name {
    position: absolute;
    font-family: "Cinzel", serif; font-weight: 700;
    color: var(--green); line-height: 1;
  }
  .brand-name .brand-line { display: block; }
  .brand-name .brand-sub { letter-spacing: .32em; }

  /* front */
  .front-brand { right: 40px; top: 126px; text-align: left; }
  .front-brand .brand-main { font-size: 38px; }
  .front-brand .brand-sub { font-size: 16px; margin-top: 8px; }
  .front-mark {
    position: absolute; right: 238px; top: 40px;
    width: 70px; height: 70px; border-radius: 50%;
    border: 7px solid var(--green);
  }
  .fully-insured {
    position: absolute; right: 36px; top: 240px;
    font-family: "Cinzel", serif; font-weight: 600; font-size: 15px;
    color: var(--text-light); letter-spacing: .04em;
  }
  .contact-name {
    position: absolute; left: 40px; top: 222px;
    font-family: "Cinzel", serif; font-weight: 700; font-size: 19px;
    color: var(--green); letter-spacing: .03em;
  }
  .contact-row {
    position: absolute; left: 40px; top: 262px;
    display: flex; gap: 26px;
    font-family: "Crimson Text", serif; font-size: 17px;
    color: var(--text-light);
  }
  .contact-item { display: flex; align-items: center; gap: 8px; }
  .contact-icon { width: 18px; height: 18px; }
  .tagline {
    position: absolute; left: 40px; top: 330px;
    font-family: "Crimson Text", serif; font-size: 19px;
    color: var(--text-light);
  }

  /* back */
  .back-brand { left: 34px; top: 62px; }
  .back-brand .brand-main { font-size: 46px; }
  .back-brand .brand-sub { font-size: 19px; margin-top: 10px; }
  .back-mark {
    position: absolute; left: 470px; top: 50px;
    width: 210px; height: 210px; border-radius: 50%;
    background: var(--card-white);
    border: 16px solid var(--green);
  }
  .services { position: absolute; left: 40px; top: 232px; }
  .services-title {
    font-family: "Cinzel", serif; font-weight: 700; font-size: 18px;
    color: var(--green); margin-bottom: 4px;
  }
  .services-list {
    list-style: none;
    font-family: "Crimson Text", serif; font-size: 15.5px; line-height: 17px;
    color: var(--text-dark);
  }
  .services-list li { position: relative; padding-left: 20px; }
  .services-list li::before {
    content: ""; position: absolute; left: 4px; top: 6px;
    width: 6px; height: 6px; border-radius: 50%; background: var(--green);
  }
</style>
</head>
<body>

<section class="card card-front" aria-label="Front of business card">
  <svg class="shapes" width="700" height="400" viewBox="0 0 700 400" aria-hidden="true">
    <line x1="180" y1="300" x2="480" y2="300" stroke="var(--green)" stroke-width="2"/>
    <polygon points="0,316 470,316 512,270 700,270 700,362 0,362" fill="var(--green)"/>
  </svg>

  <div class="front-mark" aria-hidden="true"></div>
  <h1 class="brand-name front-brand">
    <span class="brand-line brand-main">Bright Meadow</span>
    <span class="brand-line brand-sub">Lawn &amp; Landscape</span>
  </h1>

  <p class="fully-insured">Fully Insured</p>

  <p class="contact-name">Tom Berrigan</p>
  <div class="contact-row">
    <span class="contact-item">
      <svg class="contact-icon" viewBox="0 0 18 18" aria-hidden="true">
        <circle cx="9" cy="9" r="8" fill="none" stroke="var(--green)" stroke-width="1.5"/>
        <rect x="6" y="4.5" width="6" height="9" rx="1.2" fill="none" stroke="var(--text-light)" stroke-width="1.3"/>
      </svg>
      410-555-0198
    </span>
    <span class="contact-item">
      <svg class="contact-icon" viewBox="0 0 18 18" aria-hidden="true">
        <circle cx="9" cy="9" r="8.5" fill="var(--green)"/>
        <rect x="4.5" y="6" width="9" height="6.5" fill="none" stroke="var(--card-black)" stroke-width="1.2"/>
        <polyline points="4.5,6 9,10 13.5,6" fill="none" stroke="var(--card-black)" stroke-width="1.2"/>
      </svg>
      Tberrigan07@mailbox-example.com
    </span>
  </div>

  <p class="tagline">Complete Residential &amp; Commercial Landscape Services</p>
</section>

<section class="card card-back" aria-label="Back of business card">
  <svg class="shapes" width="700" height="400" viewBox="0 0 700 400" aria-hidden="true">
    <polygon points="0,0 700,0 700,112 0,212" fill="var(--card-black)"/>
    <polygon points="0,212 700,112 700,120 0,220" fill="var(--green)"/>
  </svg>

  <h2 class="brand-name back-brand">
    <span class="brand-line brand-main">Bright Meadow</span>
    <span class="brand-line brand-sub">Lawn &amp; Landscape</span>
  </h2>
  <div class="back-mark" aria-hidden="true"></div>

  <div class="services">
    <h3 class="services-title">Services We Offer</h3>
    <ul class="services-list">
      <li>Lawn Care &amp; Mowing</li>
      <li>Hedge &amp; Shrub Trimming</li>
      <li>Leaf Removal &amp; Clean Up</li>
      <li>Aeration &amp; Sod</li>
      <li>Mulch &amp; Rock Installations</li>
      <li>Landscape Installations &amp; Renovations</li>
      <li>Commercial Snow Removal</li>
    </ul>
  </div>
</section>

</body>
</html>
```